Flyer-Design für Call Center
Zielgruppe
Lark Dialog ist ein Call Center und wir vertreiben die Fachliteratur von großen deutschen Verlagen (z.B. Brosen oder Wallmut). Unsere Telefonisten rufen in Krankenhäusern, Pflegeeinrichtungen, Kindergärten, Schulen an und bieten den leitenden Personen dort die für ihr Berufsfeld passende Fachliteratur zum kostenfreien Kennenlernen an.
Aufgrund der zahlreichen anstehenden Aufträge brauchen wir dringend neuen Teamzuwachs, insbesondere möchten wir Heidelberger Werkstudenten auf uns aufmerksam machen. Die Flyer sollen bei Erstsemesterparties oder vor den Universitätsmensen verteilt werden und die Studis ansprechen.
Ziel: Ganz viele Studenten bewerben sich um eine Stelle als Vertriebler bei Lark Dialog.
Aufgabenstellung
Den Inhalt für Vorder- und Rückseite habe ich bereits zusammengefasst, kann aber auch gekürzt / verlängert werden wenn das optisch besser wäre. (siehe pdf Dokument im Anhang)
Ich habe unseren bisherigen Flyer hinzugefügt wobei uns der nicht mehr besonders gut gefällt. Es wäre schön, ein paar junge Gesichter mit denen sich die Studenten identifizieren können auf dem Flyer zu haben. Aber lieber nicht das klassische Call Center Bild 'Hübsche lächelnde Dame mit Headset' ;-)
Schön wäre es auch visuell unseren größten Vorteil der 100% freien Arbeitszeiteinteilung hervorzuheben.

```html
<!DOCTYPE html>
<html lang="de">
<head>
<meta charset="utf-8">
<title>Lark Dialog – Werkstudenten Flyer</title>
<link href="https://fonts.googleapis.com/css2?family=Fira+Sans:wght@400;600;700;800&family=Fira+Sans+Condensed:wght@400;500;600;700&display=swap" rel="stylesheet">
<style>
  :root {
    --stage: #e4e4e4;
    --paper: #f6f6f6;
    --mint: #2ee8bf;
    --royal: #2a4fe6;
    --sky: #3bb9ef;
    --ink: #1a1a1a;
    --logo: #4aa6d9;
    --white: #ffffff;
  }
  * { margin: 0; padding: 0; box-sizing: border-box; }
  html, body { width: 1200px; height: 658px; overflow: hidden; background: var(--stage); }
  body { position: relative; font-family: "Fira Sans", sans-serif; }

  .flyer { position: absolute; top: 205px; width: 182px; height: 273px; overflow: hidden; background: var(--paper); box-shadow: 0 2px 10px rgba(0,0,0,0.08); }
  .flyer--front-a { left: 219px; }
  .flyer--back { left: 516px; }
  .flyer--front-b { left: 811px; }

  .side-band { position: absolute; left: 0; top: 0; width: 34px; height: 100%; background: var(--mint); }
  .side-url {
    position: absolute; left: 0; top: 8px; width: 34px; height: 214px;
    writing-mode: vertical-rl; transform: rotate(180deg);
    text-align: end; line-height: 34px;
    font-weight: 700; font-size: 16.5px; color: var(--white); letter-spacing: 0.1px;
  }

  .photo { position: absolute; left: 34px; top: 0; width: 148px; height: 100%; }
  .photo--student-woman {
    background:
      radial-gradient(ellipse 40px 34px at 72px 40px, rgba(120,80,55,0.55), rgba(120,80,55,0) 100%),
      radial-gradient(ellipse 30px 36px at 72px 88px, rgba(222,180,150,0.75), rgba(222,180,150,0) 100%),
      radial-gradient(ellipse 90px 110px at 75px 210px, rgba(255,255,255,0.95), rgba(255,255,255,0) 100%),
      linear-gradient(160deg, #efefef 0%, #e6e4e2 60%, #e9e9e9 100%);
  }
  .photo--student-man {
    background:
      radial-gradient(ellipse 36px 30px at 102px 42px, rgba(110,72,45,0.6), rgba(110,72,45,0) 100%),
      radial-gradient(ellipse 30px 38px at 102px 88px, rgba(214,170,140,0.75), rgba(214,170,140,0) 100%),
      radial-gradient(ellipse 110px 140px at 100px 230px, rgba(95,70,50,0.85), rgba(95,70,50,0) 100%),
      linear-gradient(160deg, #e4e5ea 0%, #dcdde2 45%, #c8bcb0 100%);
  }

  .brand { position: absolute; font-family: "Fira Sans", sans-serif; font-weight: 400; font-size: 6.2px; letter-spacing: 0.4px; color: var(--logo); text-transform: uppercase; }
  .flyer--front-a .brand, .flyer--front-b .brand { left: 44px; top: 11px; }
  .flyer--back .brand { left: 120px; top: 258px; }

  .bubble { position: absolute; border-radius: 50%; display: flex; flex-direction: column; align-items: center; justify-content: center; text-align: center; color: var(--white); font-family: "Fira Sans", sans-serif; font-weight: 700; line-height: 1.1; }
  .bubble--royal { background: var(--royal); }
  .bubble--sky { background: var(--sky); }
  .bubble--mint { background: var(--mint); }
  .tilt { transform: rotate(-12deg); }

  .bubble-apply { left: 47px; top: 139px; width: 63px; height: 66px; font-size: 6.6px; }
  .bubble-wanted { left: 80px; top: 178px; width: 83px; height: 86px; }
  .bubble-wanted .wanted { font-size: 16px; font-weight: 800; line-height: 1; }
  .bubble-wanted .role { font-size: 6.8px; margin-top: 3px; }
  .bubble-welcome { left: 117px; top: 153px; width: 63px; height: 66px; font-size: 7px; }
  .flyer--front-b .bubble-wanted { left: 51px; top: 176px; }

  .back-content { position: absolute; left: 10px; top: 12px; width: 168px; color: var(--ink); }
  .tagline { font-family: "Fira Sans Condensed", sans-serif; font-weight: 700; font-size: 4.5px; color: var(--royal); }
  .headline { font-family: "Fira Sans Condensed", sans-serif; font-weight: 700; color: var(--sky); line-height: 1.18; letter-spacing: -0.1px; }
  .headline--main { font-size: 10.6px; margin-top: 8px; }
  .headline--sub { font-size: 8.6px; margin-top: 7px; margin-left: 1px; }
  .body-copy { font-family: "Fira Sans Condensed", sans-serif; font-weight: 500; font-size: 4.4px; line-height: 1.62; margin-top: 6px; margin-left: 1px; }
  .list-title { font-family: "Fira Sans Condensed", sans-serif; font-weight: 700; font-size: 4.5px; color: var(--royal); margin-top: 7px; margin-left: 1px; }
  .perks { list-style: none; font-family: "Fira Sans Condensed", sans-serif; font-weight: 500; font-size: 4.4px; line-height: 1.66; margin-left: 1px; margin-top: 1px; }
  .perks li::before { content: "• "; }
  .list-title--offer { margin-top: 6px; }

  .bubble-hours { left: 136px; top: 142px; width: 40px; height: 42px; font-weight: 400; font-size: 3.6px; line-height: 1.3; }
  .bubble-call { left: 113px; top: 173px; width: 44px; height: 47px; font-size: 4.4px; }
  .bubble-call .phone { font-weight: 400; font-size: 5.2px; margin-top: 2px; color: var(--sky); }

  .contact { position: absolute; left: 11px; top: 256px; font-family: "Fira Sans Condensed", sans-serif; font-weight: 500; font-size: 3.8px; line-height: 1.45; color: var(--sky); }
</style>
</head>
<body>

  <section class="flyer flyer--front-a">
    <div class="photo photo--student-woman" role="img" aria-label="Foto: junge Studentin im weißen T-Shirt zeigt lächelnd auf sich selbst"></div>
    <div class="side-band"></div>
    <div class="side-url">larkdialog-jobs.de</div>
    <div class="brand">Lark Dialog</div>
    <div class="bubble bubble--royal bubble-apply"><div class="tilt">Direkt online<br>bewerben –<br>nur 2 Minuten</div></div>
    <div class="bubble bubble--sky bubble-wanted"><div class="tilt"><div class="wanted">You are<br>wanted!</div><div class="role">Werkstudenten<br>gesucht</div></div></div>
  </section>

  <section class="flyer flyer--back">
    <div class="back-content">
      <p class="tagline">Lark Dialog sucht Verstärkung (m/w) für das Team in Heidelberg.</p>
      <h1 class="headline headline--main">Freie Zeiteinteilung,<br>abwechslungsreiche Aufgaben &amp;<br>ein lockeres Arbeitsklima</h1>
      <p class="body-copy">Wir zählen zu den führenden Dienstleistern für Verlagsmarketing in Deutschland und planen erfolgreiche Telefonmarketing Kampagnen für bekannte deutsche Verlage wie z.B. die Brosen Gruppe. Im Zuge dieser Kampagnen führen wir Gespräche mit interessierten Entscheidungsträgern aus Schulen, Kindertageseinrichtungen und Krankenhäusern und bieten Lösungen für die jeweiligen beruflichen Schwerpunkte in Form hochwertiger Fachliteratur an.</p>
      <h2 class="headline headline--sub">Studium oder andere Verpflichtungen,<br>trotzdem langfristig Kohle und Arbeits-<br>zeiten selbst bestimmen?</h2>
      <p class="list-title">Du punktest bei uns:</p>
      <ul class="perks">
        <li>mit einer sehr guten Ausdrucksweise</li>
        <li>viel Spaß am Kundenkontakt</li>
        <li>einer hohen Eigenmotivation</li>
        <li>Kommunikationsstärke und Fingerspitzengefühl</li>
      </ul>
      <p class="list-title list-title--offer">Wir bieten Dir …</p>
      <ul class="perks">
        <li>freie Zeiteinteilung (8–20 Std./Woche)</li>
        <li>je nach Wunsch und zu selbst bestimmten Zeiten</li>
        <li>einen unbefristeten Arbeitsvertrag</li>
        <li>eine intensive Begleitung in der Einarbeitungsphase</li>
        <li>ein ziemlich cooles Team und Spaß bei der Arbeit</li>
        <li>ein Festgehalt von 10,00€/Std.</li>
      </ul>
    </div>
    <div class="bubble bubble--mint bubble-hours"><div class="tilt">Öffnungszeiten:<br>Mo–Do 8:00–18:00 &amp;<br>Fr 8:00–15:00 Uhr</div></div>
    <div class="bubble bubble--royal bubble-call"><div class="tilt">Direkt anrufen<br>und Job<br>klar machen:<div class="phone">06221/58213</div></div></div>
    <p class="contact">Lindenweg 12 | 69117 Heidelberg<br>job@larkdialog.de | www.larkdialog.de</p>
    <div class="brand">Lark Dialog</div>
  </section>

  <section class="flyer flyer--front-b">
    <div class="photo photo--student-man" role="img" aria-label="Foto: junger Student mit Brille und kariertem Hemd zeigt lächelnd zur Seite"></div>
    <div class="side-band"></div>
    <div class="side-url">larkdialog-jobs.de</div>
    <div class="brand">Lark Dialog</div>
    <div class="bubble bubble--royal bubble-welcome">Wir freuen<br>uns auf Dich!</div>
    <div class="bubble bubble--sky bubble-wanted"><div class="wanted">You are<br>wanted!</div><div class="role">Werkstudenten<br>gesucht</div></div>
  </section>

</body>
</html>
```